Brivane - Business Cards for a new venture

create business card for a startup classified business dealing in construction materials, the cards need to have a professional look but modern, more serious than playful, one of the samples must include the official font (attached), please explore using the official colors in the company's logo

Target Market(s)

Energy sector

Contact Information for Business Card

Font styles to use
Other font styles liked:
• suissnord

Requirements
Must have
• corporate colors (in logo attached)
Nice to have
• Official font (in one of the samples) font is : suissnord
Should not have
• Cartoonish look

```html
<!DOCTYPE html>
<html lang="en">
<head>
<meta charset="utf-8">
<title>Brivane Business Card</title>
<link rel="stylesheet" href="https://fonts.googleapis.com/css2?family=Exo+2:wght@400;500;600&display=swap">
<style>
  :root{
    --blue:#33578a;
    --grey:#9b9b9b;
    --grey-light:#b4b4b4;
    --icon-grey:#8e8e8e;
    --ink-soft:#666666;
    --card:#ffffff;
    --edge:#4a4a4a;
    --page:#ececea;
  }
  *{margin:0;padding:0;box-sizing:border-box}
  html,body{width:1200px;height:1200px;overflow:hidden;background:var(--page)}
  body{position:relative;font-family:"Exo 2",sans-serif;color:var(--blue)}
  .card{position:absolute;left:188px;width:869px;height:510px;background:var(--card);border:1px solid var(--edge);overflow:hidden}
  .card--front{top:79px}
  .card--back{top:638px}
  .band{position:absolute;left:0;width:100%;height:29px;display:flex}
  .band--top{top:0}
  .band--bottom{bottom:0}
  .band__bar{flex:1;background:var(--blue)}
  .band__pattern{width:230px;background:linear-gradient(90deg,var(--grey),var(--grey-light))}
  .band__pattern--left{background:linear-gradient(90deg,var(--grey-light),var(--grey))}
  .brand-name{position:absolute;left:0;right:0;top:215px;text-align:center;font-size:60px;font-weight:500;letter-spacing:10px;color:var(--blue)}
  .row{position:absolute;left:0;width:100%}
  .icon{position:absolute;left:55px;width:43px;height:33px;background:var(--icon-grey);display:flex;align-items:center;justify-content:center}
  .icon svg{width:20px;height:20px;fill:#fff}
  .text{position:absolute;left:125px;font-size:25px;line-height:31px;white-space:nowrap;color:var(--blue)}
  .person-name{font-size:32px;line-height:36px;top:-6px}
  .person-name b{font-weight:600}
  .person-role{top:32px;font-size:21.5px;line-height:26px;color:var(--ink-soft)}
</style>
</head>
<body>

<section class="card card--front">
  <div class="band band--top">
    <div class="band__pattern band__pattern--left" role="img" aria-label="Grey diagonal stripe pattern"></div>
    <div class="band__bar"></div>
  </div>
  <div class="brand-name">BRIVANE</div>
  <div class="band band--bottom">
    <div class="band__bar"></div>
    <div class="band__pattern" role="img" aria-label="Grey diagonal stripe pattern"></div>
  </div>
</section>

<section class="card card--back">
  <div class="band band--top">
    <div class="band__bar"></div>
    <div class="band__pattern" role="img" aria-label="Grey diagonal stripe pattern"></div>
  </div>

  <div class="row" style="top:67px">
    <span class="icon"><svg viewBox="0 0 20 20"><circle cx="10" cy="6.5" r="4"/><path d="M2 18c0-4 3.5-6.5 8-6.5s8 2.5 8 6.5z"/></svg></span>
    <div class="text person-name"><b>Arun</b> Mehta</div>
    <div class="text person-role">Managing Director</div>
  </div>

  <div class="row" style="top:156px">
    <span class="icon"><svg viewBox="0 0 20 20"><path d="M5 2l3 4-2 2c1 2.5 3 4.5 5.5 5.5l2-2 4 3-2 3C9 17 3 11 2 5z"/></svg></span>
    <div class="text" style="top:1px">+91 7800 425 118</div>
  </div>

  <div class="row" style="top:217px">
    <span class="icon"><svg viewBox="0 0 20 20"><path d="M10 1a6 6 0 0 1 6 6c0 4.5-6 12-6 12S4 11.5 4 7a6 6 0 0 1 6-6zm0 3.5a2.5 2.5 0 1 0 0 5 2.5 2.5 0 0 0 0-5z"/></svg></span>
    <div class="text" style="top:1px">Brivane, Near Crest Building, Lakeview Road, Ravipur</div>
  </div>

  <div class="row" style="top:286px">
    <span class="icon"><svg viewBox="0 0 20 20"><path d="M10 2l9 8h-3v8h-4.5v-5h-3v5H4v-8H1z"/></svg></span>
    <div class="text" style="top:-6px">Opp. Orion Tower, Near City Central Bank,<br>Lakeview Road, Ravipur, Westland, India.</div>
  </div>

  <div class="row" style="top:382px">
    <span class="icon"><svg viewBox="0 0 20 20" stroke="#fff" stroke-width="1.4" style="fill:none"><rect x="2" y="4.5" width="16" height="11"/><path d="M2 4.5l8 6.5 8-6.5M2 15.5l6-5.5M18 15.5l-6-5.5"/></svg></span>
    <div class="text" style="top:-1px">Info@brivane.com</div>
  </div>

  <div class="row" style="top:443px">
    <span class="icon"><svg viewBox="0 0 20 20" style="fill:none" stroke="#fff" stroke-width="1.3"><circle cx="10" cy="10" r="7.5"/><ellipse cx="10" cy="10" rx="3.2" ry="7.5"/><path d="M2.5 10h15M4 6h12M4 14h12"/></svg></span>
    <div class="text" style="top:1px">www.brivane.com</div>
  </div>
</section>

</body>
</html>
```